Web Design Project for starting CCTV/Camera security installer/reseller

Hello,

An old class mate is starting his own little CCTV/Camera security business as a one-man-gang.

He asked me to do his website but unfortunatly my design skills are not worth looking at :) The coding is no problem.

So I'm here to request a design.

What he wants is a site that lists the products he might install which is based on a small tree structure. So see it as a shop overview/display but without the baskets & cashout options.

you can find a site structure scheme, logo, product images & data sheet pdf's at this filvaultra address:

https://www.filvaultra.com/sh/kq7zt3908wx4pl2/vnRtLoBe5y/Lumo-Ward

the site itself is http://www.lumo-ward.be but only has a splash screen until I have a design for it.

the logo is a bit out of proportions, not sure if you can make something good out of it :/

Most content is in Dutch, I'll see if I can translate the needed parts...
Updates

Dear designers,

I have some good new for you.

You are allowed to use only that chrome Lumo-Ward part of the logo,
which should make things a lot easier to fit into your design ideas.

Keep up the creativity!

Dear designers,

I uploaded a new logo to the filvaultra space.

It's a png but unfortunately it's not transparent, I'm still waiting for that one
but you know how to erase it in photoshop.

Target Market(s)

people looking for a visual solution to protect their company/home

Industry/Entity Type

Security

Requirements
Must have
• an iconized way to browse/display a tree. (not the traditional folder/explorer style)

maybe first a page with buttons/icons showing level 1 the group types (IP cams, IP servers, Accessories)

level 2 product groups (dome cam, ptz cam etc)

level 3 the actual product + a link to a pdf datasheet (if any)

could be multipage or maybe in/on-page since the product list won't be that huge.

maybe some random product info left and/or right so that the content area is not massive since he has not much to type
;)

```html
<!DOCTYPE html>
<html lang="en">
<head>
<meta charset="utf-8">
<title>Lumo-Ward – Camera surveillance</title>
<link href="https://fonts.googleapis.com/css2?family=Open+Sans:wght@400;600;700&family=Oswald:wght@300;400&family=Libre+Baskerville&display=swap" rel="stylesheet">
<style>
:root{
  --navy:#0b2f7a;
  --blue:#1560b4;
  --blue-mid:#1d68c4;
  --blue-light:#dcecf8;
  --ink:#2a2a2a;
  --heading:#1a3c86;
  --panel-line:#d5dde8;
  --white:#ffffff;
  --field:#ececec;
}
*{box-sizing:border-box;margin:0;padding:0}
html,body{width:1126px;height:1200px;overflow:hidden}
body{position:relative;background:var(--white);font-family:"Open Sans",Arial,sans-serif;color:var(--ink)}
.abs{position:absolute}
.header{left:0;top:0;width:1126px;height:125px;background:linear-gradient(#d7ebf8,#ffffff 85%)}
.top-stripe{left:0;top:0;width:1126px;height:4px;background:linear-gradient(90deg,#7fb3e6 0 12%,var(--navy) 12% 25%,#7fb3e6 25% 37%,var(--navy) 37% 50%,#7fb3e6 50% 62%,var(--navy) 62% 75%,#7fb3e6 75% 87%,var(--navy) 87%)}
.brand{left:22px;top:46px;display:flex;align-items:center;gap:8px;font-weight:600;font-size:21px;color:var(--navy)}
.brand-dot{width:26px;height:26px;border-radius:50%;background:var(--blue)}
.account-btn{top:29px;height:27px;border-radius:5px;background:linear-gradient(#1a56b0,#0c3583);color:#fff;font-size:12px;display:flex;align-items:center;justify-content:center}
.social{top:68px;width:26px;height:26px;border-radius:5px}
.nav{left:20px;top:127px;width:1087px;height:49px;border-radius:6px;background:linear-gradient(#1f5fb8,#0d3f95)}
.nav-item{top:0;height:49px;line-height:52px;color:#fff;font-size:17px;transform:translateX(-50%)}
.nav-home{left:19px;top:6px;width:84px;height:43px;border-radius:5px 5px 0 0;background:linear-gradient(#f4f9fd,#d6e8f6);color:var(--blue);font-size:17px;text-align:center;line-height:42px}
.search{left:891px;top:9px;width:172px;height:27px;border-radius:14px;background:#0a3b8e;border:1px solid #4d86d4}
.hero-photo{left:491px;top:192px;width:616px;height:293px;border-radius:4px;border:2px solid #fff;background:linear-gradient(160deg,#2d6fc6,#9cc7ee 45%,#e8f2fb 60%,#3b79c4);box-shadow:-14px 18px 22px rgba(0,0,0,.22)}
.hero-line1{left:51px;top:252px;font-family:"Oswald",sans-serif;font-weight:300;font-size:34px;color:var(--heading);letter-spacing:.2px}
.hero-line2{left:83px;top:316px;font-weight:700;font-size:32px;color:var(--blue-mid)}
.hero-line3{left:126px;top:367px;font-weight:700;font-size:32px;color:var(--blue-mid)}
.read-more{left:83px;top:425px;width:130px;height:32px;border-radius:6px;background:linear-gradient(#2a67ba,#0e3a84);color:#fff;font-family:"Oswald",sans-serif;font-weight:300;font-size:16px;display:flex;align-items:center;padding-left:14px;gap:12px}
.categories{left:21px;top:551px;width:543px;height:248px;border:1px solid var(--panel-line);border-radius:6px}
.cat-icon{top:571px;width:87px;height:107px}
.cat-label{top:699px;width:132px;height:74px;border-radius:8px;background:linear-gradient(var(--blue-light),#fff);border:1px solid #e0e9f2;color:var(--blue);font-weight:700;font-size:16px;display:flex;align-items:center;justify-content:center}
.cat-label::before{content:"";position:absolute;left:50%;top:-12px;margin-left:-10px;border:10px solid transparent;border-top:0;border-bottom:12px solid var(--blue-light)}
.pager{top:786px;width:24px;height:24px}
.welcome-title{left:596px;top:546px;font-weight:700;font-size:20px;color:var(--blue)}
.points{left:598px;top:590px;width:500px;list-style:none;font-size:13px;line-height:19.5px;color:#333}
.points li{position:relative;padding-left:36px}
.points svg{position:absolute;left:0;top:0}
.footer-head{left:0;top:876px;width:1126px;height:46px;background:var(--navy)}
.footer-body{left:0;top:922px;width:1126px;height:232px;background:radial-gradient(ellipse at 50% 100%,#3d86d6,#1a5cb4 55%,#10479b)}
.footer-bottom{left:0;top:1154px;width:1126px;height:46px;background:var(--navy)}
.footer-title{top:888px;font-family:"Libre Baskerville",serif;font-size:17px;color:#fff}
.footer-text{font-family:Arial,Helvetica,sans-serif;font-size:13px;line-height:19.5px;color:#fff}
.footer-btn{left:37px;top:1052px;width:95px;height:29px;border-radius:5px;background:linear-gradient(#3a7bd0,#1a509f);border:1px solid #0c3a82;color:#0c2c66;font-family:Arial,sans-serif;font-size:13px;display:flex;align-items:center;justify-content:center}
.field{left:848px;width:235px;height:29px;border-radius:5px;background:var(--field);color:#222;font-family:Arial,sans-serif;font-size:13px;padding-left:12px;display:flex;align-items:center}
.field-select::after{content:"";position:absolute;right:0;top:0;width:29px;height:29px;border-radius:0 5px 5px 0;background:var(--navy)}
.caret{position:absolute;right:9px;top:12px;z-index:1;border:5px solid transparent;border-top:6px solid #fff;border-bottom:0}
.submit{left:995px;top:1121px;width:93px;height:28px;border-radius:6px;background:linear-gradient(#4d8fe0,#1f5fb8);border:1px solid #0c3a82;color:#0c2c66;font-family:Arial,sans-serif;font-size:13px;display:flex;align-items:center;justify-content:center}
.footer-badge{left:518px;top:1107px;width:82px;height:82px;border-radius:50%;background:#fff;box-shadow:0 0 14px rgba(160,210,255,.9);display:flex;align-items:center;justify-content:center;font-weight:600;font-size:13px;color:var(--navy)}
.copyright{left:20px;top:1172px;font-family:Arial,sans-serif;font-size:12.5px;color:#fff}
.legal{right:20px;top:1170px;font-family:Arial,sans-serif;font-size:12.5px;color:#fff}
</style>
</head>
<body>

<header class="abs header"></header>
<div class="abs top-stripe"></div>
<div class="abs brand"><span class="brand-dot"></span>Lumo-Ward</div>

<div class="abs account-btn" style="left:989px;width:49px">Jion</div>
<div class="abs account-btn" style="left:1049px;width:55px">Login</div>
<div class="abs social" style="left:970px;background:#3b5ea8"></div>
<div class="abs social" style="left:1005px;background:#45b3d8"></div>
<div class="abs social" style="left:1041px;background:#1d5c94"></div>
<div class="abs social" style="left:1078px;background:#e8752a"></div>

<nav class="abs nav">
  <div class="abs nav-home">Home</div>
  <span class="abs nav-item" style="left:194px">About Us</span>
  <span class="abs nav-item" style="left:338px">Services</span>
  <span class="abs nav-item" style="left:458px">tips</span>
  <span class="abs nav-item" style="left:587px">products</span>
  <span class="abs nav-item" style="left:740px">Contact Us</span>
  <div class="abs search">
    <svg class="abs" style="left:11px;top:6px" width="14" height="14" viewBox="0 0 14 14"><circle cx="5.5" cy="5.5" r="4" fill="none" stroke="#fff" stroke-width="2"/><line x1="8.5" y1="8.5" x2="12" y2="12" stroke="#fff" stroke-width="2"/></svg>
  </div>
</nav>

<div class="abs hero-line1">LOREM IPSUM DOLOR SIT AMET</div>
<div class="abs hero-line2">LOREM IPSUM DOLOR SIT</div>
<div class="abs hero-line3">LOREM IPSUM DOLOR</div>
<div class="abs read-more">READ MORE
  <svg width="20" height="20" viewBox="0 0 20 20"><circle cx="10" cy="10" r="9" fill="#fff"/><path d="M8 5.5l5.5 4.5L8 14.5z" fill="#14428e"/></svg>
</div>
<div class="abs hero-photo" role="img" aria-label="Security cameras and dome cameras against glass office towers and a blue sky"></div>

<section class="abs categories"></section>

<svg class="abs cat-icon" style="left:63px" viewBox="0 0 87 107"><path d="M6 2h58l21 21v78a4 4 0 0 1-4 4H6a4 4 0 0 1-4-4V6a4 4 0 0 1 4-4z" fill="#fff" stroke="#1d3f80" stroke-width="3"/><path d="M64 2v21h21" fill="none" stroke="#1d3f80" stroke-width="3"/><rect x="27" y="47" width="32" height="25" rx="3" fill="#222"/><path d="M59 53l9-5v22l-9-5z" fill="#222"/><circle cx="32" cy="42" r="6" fill="#222"/><circle cx="47" cy="42" r="6" fill="#222"/><rect x="17" y="55" width="10" height="8" fill="#222"/><rect x="35" y="60" width="14" height="5" fill="#fff"/></svg>
<svg class="abs cat-icon" style="left:248px" viewBox="0 0 87 107"><path d="M6 2h58l21 21v78a4 4 0 0 1-4 4H6a4 4 0 0 1-4-4V6a4 4 0 0 1 4-4z" fill="#fff" stroke="#1d3f80" stroke-width="3"/><path d="M64 2v21h21" fill="none" stroke="#1d3f80" stroke-width="3"/><path d="M13 40v38h62" fill="none" stroke="#222" stroke-width="2.5"/><g fill="#222"><rect x="19" y="64" width="6" height="12"/><rect x="28" y="60" width="6" height="16"/><rect x="37" y="62" width="6" height="14"/><rect x="46" y="56" width="6" height="20"/><rect x="55" y="52" width="6" height="24"/><rect x="64" y="46" width="6" height="30"/></g><path d="M18 60l12-8 10 4 12-10 13-8" fill="none" stroke="#222" stroke-width="2.5"/><path d="M60 34l9 1-3 8z" fill="#222"/></svg>
<svg class="abs cat-icon" style="left:435px" viewBox="0 0 87 107"><path d="M6 2h58l21 21v78a4 4 0 0 1-4 4H6a4 4 0 0 1-4-4V6a4 4 0 0 1 4-4z" fill="#fff" stroke="#1d3f80" stroke-width="3"/><path d="M64 2v21h21" fill="none" stroke="#1d3f80" stroke-width="3"/><rect x="17" y="42" width="52" height="38" rx="6" fill="none" stroke="#222" stroke-width="4"/><rect x="33" y="35" width="20" height="8" rx="2" fill="#222"/><circle cx="43" cy="61" r="13" fill="none" stroke="#222" stroke-width="4"/><circle cx="43" cy="61" r="6" fill="none" stroke="#222" stroke-width="3"/></svg>

<div class="abs cat-label" style="left:41px">CAMS</div>
<div class="abs cat-label" style="left:226px">SERVER</div>
<div class="abs cat-label" style="left:413px">ACCESOIRES</div>

<svg class="abs pager" style="left:60px" viewBox="0 0 24 24"><circle cx="12" cy="12" r="11" fill="#eef1f4" stroke="#b8bfc8"/><path d="M14.5 7l-6 5 6 5z" fill="#a4acb6"/></svg>
<svg class="abs pager" style="left:502px" viewBox="0 0 24 24"><circle cx="12" cy="12" r="11" fill="#eef1f4" stroke="#b8bfc8"/><path d="M9.5 7l6 5-6 5z" fill="#a4acb6"/></svg>

<h2 class="abs welcome-title">Welcome at Lumo-Ward Camera surveilance</h2>
<ul class="abs points">
  <li style="margin-bottom:32px"><svg width="22" height="20" viewBox="0 0 22 20"><path d="M2 11l6 7L21 2 8 13z" fill="#1a4ea0"/></svg>Are you looking for a camera system for your home or company?</li>
  <li style="margin-bottom:32px"><svg width="22" height="20" viewBox="0 0 22 20"><path d="M2 11l6 7L21 2 8 13z" fill="#1a4ea0"/></svg>Then you are at Lumo-Ward at the right address!</li>
  <li style="margin-bottom:14px"><svg width="22" height="20" viewBox="0 0 22 20"><path d="M2 11l6 7L21 2 8 13z" fill="#1a4ea0"/></svg>We offer a large amount of surveilance camera’s, video storage systems and surveilance monitors</li>
  <li><svg width="22" height="20" viewBox="0 0 22 20"><path d="M2 11l6 7L21 2 8 13z" fill="#1a4ea0"/></svg>But we also have complete camera surveillance sets for you (analogue or IP camera’s) including the cables and power supplies, so that you don’t have to worry about additional components when ordering</li>
</ul>

<footer>
  <div class="abs footer-head"></div>
  <div class="abs footer-body"></div>
  <div class="abs footer-bottom"></div>

  <h3 class="abs footer-title" style="left:37px">News &amp; Events</h3>
  <h3 class="abs footer-title" style="left:297px">Products</h3>
  <h3 class="abs footer-title" style="left:616px">Contact Us</h3>
  <h3 class="abs footer-title" style="left:848px">Quick Contact</h3>

  <div class="abs footer-text" style="left:37px;top:940px">Sydney<br>Lorem ispum dumy text</div>
  <div class="abs footer-text" style="left:37px;top:995px">Melbourne<br>Lorem ispum dumy text</div>
  <div class="abs footer-btn">Read more</div>

  <p class="abs footer-text" style="left:297px;top:940px;width:250px">Lorem ipsum dolor sit amet, consectetur adipiscing elit. Integer semper leo ac urna sodales vulputate. Donec posuere risus sit amet nisl pharetra ac facilisis nisl placerat.</p>

  <address class="abs footer-text" style="left:616px;top:940px;font-style:normal;line-height:24px">Lumo Ward Security<br>Veldhovenlaan 42<br>9470 Brakelmonde<br>Belgium<br>T: +32 470 55 20 18</address>

  <div class="abs field" style="top:939px">Full Name</div>
  <div class="abs field" style="top:978px">Email Address</div>
  <div class="abs field field-select" style="top:1020px">Send Email to:<span class="caret"></span></div>
  <div class="abs field field-select" style="top:1061px">The subject of this email:<span class="caret"></span></div>
  <div class="abs footer-text" style="left:860px;top:1095px">Your question or comments</div>
  <div class="abs submit">Submit</div>

  <div class="abs footer-badge">Lumo-Ward</div>

  <div class="abs copyright">© Copyright Lumo-Ward 2012 -2013 , All Rights Reserved</div>
  <div class="abs legal">TERMS &amp; CONDITIONS | PRIVACY POLICY</div>
</footer>

</body>
</html>
```